Brick Paving Company - Pickup Truck and Trailer Wrap Design

**Project Overview:**
We are a brick paving company, specializing in creating beautiful paver patios, walkways, and retaining walls. We're seeking a talented designer on ArtFolio to create a striking partial or full wrap design for our white pickup truck and trailer. This project demands a balance of creative flair, brand alignment, and a focus on showcasing our services in a visually appealing and professional manner.
**Objectives:**
1. **Brand Consistency:** Employ our provided brand guide and logo to ensure the design aligns with our company's identity.
2. **Flexible Wrap Design:** While our initial preference is for a partial wrap due to budget considerations, we are open to a full wrap design if it significantly enhances the impact and is cost-justifiable.
3. **Service Representation:** Clearly highlight our core services (paver patios, walkways, retaining walls) within the design in an engaging and understandable manner.
4. **Website Synergy:** Take inspiration from the aesthetics of our website for design consistency.
5. **Cost-Effective Solutions:** Prioritize designs that offer the best value for money, balancing visual appeal and budget constraints.

We are excited to see innovative designs that make our company's vehicles stand out, effectively promoting our services.

SEE ATTACHED PHOTOS AND GUIDE

Truck is a 2023 Velkor Tundrax 4200 with Dullies
Trailer is Summit Haul - you will need to use the attached measuring guide with these measurements provided in inches.

87 3/4 width, 78 1/2 height

A - 191
B - 129 1/2
C - 191
D - 2 7/8
E - 2 3/4
F - 17 1/4 & 7 3/8
G - 38 3/8
H - 75 1/4
I - 85 3/4
J - 68 5/8
K - 12 3/4
L - 5
M - 64 1/2
N - 51
O - 51

Target Market(s)

Please see the Ideal Customer Profile that is attached

Industry/Entity Type

Brick Paving, Hardscape, Outdoor Living

Requirements
Must have
• Include our phone #(866) 394-5081. phone # 866-39-STONE
Nice to have
• Simple and Eye Catching

```html
<!DOCTYPE html>
<html lang="en">
<head>
<meta charset="utf-8">
<title>Harbor Brick Paving – Vehicle Wrap Panel</title>
<link rel="stylesheet" href="https://fonts.googleapis.com/css2?family=EB+Garamond:wght@500&family=Roboto+Condensed:wght@700&display=swap">
<style>
  :root {
    --brick: #d08c3a;
    --brick-deep: #c8842f;
    --mortar: #333132;
    --ink-light: #ffffff;
  }
  html, body {
    margin: 0;
    padding: 0;
    overflow: hidden;
    background: var(--mortar);
  }
  .wrap-panel {
    position: relative;
    width: 1200px;
    height: 928px;
    overflow: hidden;
  }
  .wall {
    position: absolute;
    inset: 0;
    background:
      repeating-linear-gradient(180deg,
        var(--mortar) 0px, var(--mortar) 5px,
        transparent 5px, transparent 29px),
      linear-gradient(180deg, var(--brick) 0%, var(--brick-deep) 100%);
  }
  .shapes {
    position: absolute;
    inset: 0;
  }
  .brand-name {
    position: absolute;
    left: 260px;
    top: 395px;
    width: 630px;
    display: flex;
    flex-direction: column;
    align-items: center;
    font-family: "EB Garamond", serif;
    font-weight: 500;
    color: var(--ink-light);
    text-align: center;
    line-height: 1;
  }
  .brand-name__main {
    font-size: 78px;
    letter-spacing: 1px;
  }
  .brand-name__sub {
    font-size: 30px;
    letter-spacing: 8px;
    margin-top: 10px;
  }
  .services {
    position: absolute;
    left: 137px;
    top: 612px;
    width: 927px;
    height: 152px;
    margin: 0;
    display: flex;
    flex-direction: column;
    align-items: center;
    justify-content: center;
    font-family: "EB Garamond", serif;
    font-weight: 500;
    font-size: 62px;
    line-height: 1.18;
    color: var(--ink-light);
    text-align: center;
    white-space: nowrap;
  }
  .contact {
    position: absolute;
    left: 132px;
    top: 815px;
    width: 873px;
    height: 73px;
    margin: 0;
    display: flex;
    align-items: center;
    justify-content: center;
    font-family: "Roboto Condensed", sans-serif;
    font-weight: 700;
    font-size: 37px;
    color: var(--ink-light);
    white-space: nowrap;
  }
</style>
</head>
<body>
<main class="wrap-panel">
  <div class="wall" role="img" aria-label="Brick wall pattern in warm orange bricks with dark mortar lines"></div>

  <svg class="shapes" width="1200" height="928" viewBox="0 0 1200 928" aria-hidden="true">
    <rect class="logo-field" x="260" y="203" width="630" height="404" fill="var(--mortar)"/>
    <circle class="logo-dot" cx="575" cy="330" r="52" fill="none" stroke="var(--brick)" stroke-width="3"/>
    <polygon class="services-banner" points="137,612 1064,612 1048,764 153,764" fill="var(--mortar)"/>
    <rect class="contact-band" x="132" y="815" width="873" height="73" fill="var(--mortar)"/>
  </svg>

  <div class="brand-name">
    <span class="brand-name__main">HARBOR BRICK</span>
    <span class="brand-name__sub">PAVING</span>
  </div>

  <h1 class="services">
    <span>BRICK PAVING, HARDSCAPE</span>
    <span>OUTDOOR LIVING</span>
  </h1>

  <p class="contact">phone #(866) 394-5081. phone # 866-39-STONE</p>
</main>
</body>
</html>
```